Business Card Design

Business Card for professional consulting firm working with large financial institutions.

Target Market(s)

Executive buyers

Industry/Entity Type

Banking

Contact Information for Business Card

Mild creativity wanted. Not boring, but do elaborate artwork.

Font styles to use
Serif
Sans Serif

Colors

Designer to choose colors to be used in the design.

Requirements
Must have
• Standard business card features - company name, individual name, telephone, website, email, locations.
Nice to have
• Two colors
Should not have
• too many colors, fancy printing, cartoons.

```html
<!DOCTYPE html>
<html lang="en">
<head>
<meta charset="utf-8">
<title>n4advisory business card</title>
<link rel="stylesheet" href="https://fonts.googleapis.com/css2?family=Tinos:wght@400&display=swap">
<style>
  :root {
    --backdrop: #a9a9a9;
    --card-white: #f1f1f1;
    --ink: #111111;
    --ink-black: #000000;
    --text-dark: #333333;
    --text-muted: #a8a8a8;
    --swoosh-grey: #bdbdbd;
    --divider: #c9c9c9;
    --white: #ffffff;
  }
  * { margin: 0; padding: 0; box-sizing: border-box; }
  html, body {
    width: 1200px; height: 960px; overflow: hidden;
    background: var(--backdrop);
  }
  .stage { position: relative; width: 1200px; height: 960px; }
  .card {
    position: absolute; width: 600px; height: 343px; overflow: hidden;
    font-family: "Tinos", "Times New Roman", serif;
  }
  .card-front { left: 322px; top: 108px; background: var(--card-white); }
  .card-back { left: 320px; top: 493px; background: var(--ink-black); }
  .front-swoosh { position: absolute; left: 0; top: 0; }
  .front-brand {
    position: absolute; left: 115px; top: 152px;
    font-size: 25px; color: var(--text-dark); letter-spacing: 0.2px;
  }
  .divider {
    position: absolute; left: 313px; top: 92px; width: 1px; height: 158px;
    background: var(--divider);
  }
  .contact { position: absolute; left: 337px; top: 92px; color: var(--text-dark); }
  .person-name { font-size: 23px; color: var(--ink); line-height: 28px; }
  .person-title { font-size: 15px; color: var(--text-muted); line-height: 16px; }
  .address { margin-top: 13px; font-size: 15px; line-height: 20px; }
  .channels { margin-top: 9px; list-style: none; font-size: 15px; line-height: 19.5px; }
  .channels li { display: flex; align-items: center; gap: 7px; }
  .channels svg { width: 13px; height: 13px; flex: none; }
  .back-brand {
    position: absolute; left: 0; right: 0; top: 138px; text-align: center;
    font-size: 50px; color: var(--white); letter-spacing: 0.5px;
  }
</style>
</head>
<body>
<main class="stage">
  <section class="card card-front">
    <svg class="front-swoosh" width="600" height="343" viewBox="0 0 600 343">
      <path d="M0,278 C8,318 60,328 160,328 L600,303 L600,343 L0,343 Z" fill="var(--ink-black)"/>
      <path d="M63,208 C10,240 -4,312 130,324 Q360,332 600,300 Q360,320 145,318 C35,308 18,252 63,208 Z"
            fill="var(--swoosh-grey)" stroke="var(--white)" stroke-width="2"/>
    </svg>
    <div class="front-brand">n4advisory</div>
    <div class="divider"></div>
    <div class="contact">
      <div class="person-name">Daniel Reyes</div>
      <div class="person-title">CEO/Founder</div>
      <div class="address">4120 Harbor View Road<br>Fairbanks, Alaska 99701</div>
      <ul class="channels">
        <li>
          <svg viewBox="0 0 16 16"><path d="M3.5 1 L6 1.5 L6.8 5 L5 6.3 C6 8.5 7.5 10 9.7 11 L11 9.2 L14.5 10 L15 12.5 C15 14 14 15 12.5 15 C6.5 14.5 1.5 9.5 1 3.5 C1 2 2 1 3.5 1 Z" fill="var(--ink)"/></svg>
          <span>555 210 4836</span>
        </li>
        <li>
          <svg viewBox="0 0 16 16"><rect x="1" y="3" width="14" height="10" fill="var(--ink)"/><path d="M1 3.5 L8 9 L15 3.5" stroke="var(--white)" stroke-width="1.2" fill="none"/></svg>
          <span>hello@n4advisory.com</span>
        </li>
        <li>
          <svg viewBox="0 0 16 16"><circle cx="8" cy="8" r="7" fill="var(--ink)"/><path d="M4 5 C6 4 7 6 6 8 C5 9 6 11 7 12 M10 3 C9 5 11 6 12 7" stroke="var(--white)" stroke-width="1.3" fill="none"/></svg>
          <span>www.n4advisory.com</span>
        </li>
      </ul>
    </div>
  </section>

  <section class="card card-back">
    <div class="back-brand">n4advisory</div>
  </section>
</main>
</body>
</html>
```